Tolvane BrandWorks Corporate Site

Design a site to replace www.tolvanebrandworks.com, built for/within net harbor and incorporate numerous corporate assets and lines of business (www.pulsarstageworksinc.com, www.summitoutingpros.com, www.zapsnapkiosk.com, www.nibblecrate.com, www.strumbleorama.com) as well as our consulting and artist management work.

Target Market(s)

businesses, non profits, talent (performing artists)

Industry/Entity Type

Business

Coding

Coded - Design and coding required

Number of Pages Required

5+ page

Colors
0655a3
ffc214

Requirements
Must have
• social media visibility, multi-media

```html
<!DOCTYPE html>
<html lang="en">
<head>
<meta charset="utf-8">
<title>Tolvane BrandWorks</title>
<link href="https://fonts.googleapis.com/css2?family=Raleway:wght@400;500;600;700&display=swap" rel="stylesheet">
<style>
:root{
  --blue:#0655a3;
  --blue-deep:#034a8e;
  --navy:#0a3168;
  --gold:#ffc214;
  --gold-dark:#e9a91a;
  --gold-text:#c98d0f;
  --ink:#4a4a4a;
  --rule:#dcdcdc;
  --white:#fff;
}
*{box-sizing:border-box;margin:0;padding:0}
html,body{width:924px;height:1200px;overflow:hidden}
body{position:relative;font-family:"Raleway",sans-serif;color:var(--ink);
  background:linear-gradient(180deg,#0a4a8f 0%,var(--blue) 45%,#0a5fb3 100%)}
.abs{position:absolute}
.panel{position:absolute;left:58px;width:809px;background:var(--white);border-radius:3px}

/* header */
.header{top:22px;height:90px}
.logo{position:absolute;left:8px;top:12px;font-size:27px;font-weight:600;color:var(--navy);letter-spacing:-.3px;white-space:nowrap}
.logo-rule{position:absolute;left:8px;top:46px;width:240px;height:1px;background:var(--navy)}
.tagline{position:absolute;left:8px;top:49px;font-size:8.3px;letter-spacing:.9px;color:#666;text-transform:uppercase;white-space:nowrap}
.search{position:absolute;left:623px;top:19px;width:168px;height:28px;border:1px solid #ccc;border-radius:2px;display:flex}
.search span{flex:1;font-size:10px;color:#999;padding:8px 0 0 11px}
.search b{width:30px;background:var(--navy);display:flex;align-items:center;justify-content:center}

.ribbon{position:absolute;left:18px;top:76px}
.nav{position:absolute;left:46px;top:89px;width:832px;height:37px;background:linear-gradient(180deg,#f7c43b,var(--gold-dark));display:flex}
.nav a{height:100%;display:flex;align-items:center;justify-content:center;color:var(--white);font-size:12.5px;font-weight:600;text-decoration:none;border-right:1px solid rgba(180,120,0,.35)}
.nav a:last-child{border-right:0}
.nav a.current{color:var(--navy);font-weight:700}

/* hero */
.hero{position:absolute;left:58px;top:132px;width:809px;height:330px;background:var(--white);padding:4px}
.hero-photo{width:100%;height:100%;background:linear-gradient(110deg,#dfe6ee 0%,#b9c6d4 30%,#2c3a52 55%,#dbe3ea 75%,#8a9bb0 100%);position:relative}
.hero-caption{position:absolute;left:127px;top:134px;padding:2px 11px 4px;background:rgba(40,40,40,.7);color:var(--white);font-size:38px;font-weight:500;letter-spacing:.5px;white-space:nowrap}
.dots{position:absolute;left:370px;top:293px;display:flex;gap:5px}
.dots i{width:11px;height:11px;border-radius:50%;background:var(--white)}
.dots i.on{background:var(--gold)}

/* features */
.features{top:478px;height:230px;display:flex;padding:22px 0 0}
.feature{flex:1;text-align:center;border-right:1px solid var(--rule);height:175px}
.feature:last-child{border-right:0}
.feature .badge{width:80px;height:80px;margin:0 auto;border-radius:50%;background:var(--gold);border:3px solid #d9d9d9}
.feature h3{margin-top:14px;font-size:18.5px;font-weight:500;color:var(--blue-deep);letter-spacing:.5px}
.feature p{margin:9px auto 0;width:240px;font-size:11px;line-height:18.5px}

/* welcome */
.welcome{top:725px;height:263px}
.welcome h2{position:absolute;left:16px;top:23px;font-size:19px;font-weight:500;color:var(--blue-deep);letter-spacing:.3px}
.welcome p{position:absolute;left:16px;top:56px;width:490px;font-size:11.3px;line-height:18.5px}
.btn{position:absolute;left:16px;top:204px;width:111px;height:30px;border-radius:3px;background:linear-gradient(180deg,#f7c43b,var(--gold-dark));color:var(--white);font-size:11px;font-weight:700;display:flex;align-items:center;justify-content:center}
.minute{position:absolute;left:553px;top:28px;width:236px}
.minute-head{height:34px;background:var(--navy);color:var(--white);font-size:17px;font-weight:600;display:flex;align-items:center;justify-content:center;letter-spacing:.3px}
.minute-logo{height:88px;background:#f2f2f2;display:flex;align-items:center;justify-content:center;gap:10px}
.minute-logo span{font-size:16px;font-weight:700;color:var(--ink);line-height:18px}
.minute-logo i{width:22px;height:22px;border-radius:50%;background:#ea5a24}
.minute-note{height:83px;background:var(--gold);color:var(--white);font-size:13.5px;font-weight:600;text-align:center;line-height:20px;padding-top:12px}

/* blog */
.blog{top:1006px;height:100px}
.blog h2{position:absolute;left:20px;top:28px;font-size:17.5px;font-weight:500;color:var(--blue-deep)}
.arrows{position:absolute;left:49px;top:59px;display:flex;gap:4px}
.arrows i{width:15px;height:15px;border-radius:50%;display:flex;align-items:center;justify-content:center}
.brace{position:absolute;left:140px;top:24px}
.post-title{position:absolute;left:168px;top:15px;font-size:14px;font-weight:500;color:var(--blue-deep)}
.post-meta{position:absolute;left:168px;top:37px;font-size:9.5px;color:var(--gold-text)}
.post-text{position:absolute;left:168px;top:52px;width:630px;font-size:11.3px;line-height:18px}

/* footer */
.foot-nav{position:absolute;left:59px;top:1131px;display:flex;gap:23px}
.foot-nav a{color:var(--white);font-size:11px;font-weight:500;text-decoration:none}
.copyright{position:absolute;left:59px;top:1158px;font-size:9.5px;color:#0f3f78}
.social{position:absolute;left:759px;top:1140px;display:flex;gap:4px}
.social i{width:24px;height:24px;border-radius:50%}
</style>
</head>
<body>

<header class="panel header">
  <div class="logo">Tolvane BrandWorks</div>
  <div class="logo-rule"></div>
  <div class="tagline">Strategic Marketing &amp; Communications</div>
  <div class="search"><span>Search..</span><b>
    <svg width="12" height="12" viewBox="0 0 12 12"><circle cx="5" cy="5" r="3.6" fill="none" stroke="#fff" stroke-width="1.6"/><line x1="7.6" y1="7.6" x2="10.8" y2="10.8" stroke="#fff" stroke-width="1.8" stroke-linecap="round"/></svg>
  </b></div>
</header>

<svg class="ribbon" width="888" height="36" viewBox="0 0 888 36">
  <polygon points="0,2 28,2 28,36 14,22" fill="#f2b320"/>
  <polygon points="888,2 860,2 860,36 874,22" fill="#f2b320"/>
  <polygon points="28,36 28,13 22,13" fill="#b07d0c"/>
  <polygon points="860,36 860,13 866,13" fill="#b07d0c"/>
</svg>

<nav class="nav">
  <a class="current" style="width:103px">Home</a>
  <a style="width:106px">About</a>
  <a style="width:143px">Our Services</a>
  <a style="width:112px">Clients</a>
  <a style="width:155px">News &amp; Events</a>
  <a style="width:101px">Blog</a>
  <a style="width:112px">Contact</a>
</nav>

<section class="hero">
  <div class="hero-photo" role="img" aria-label="Photo of business people shaking hands in a bright office">
    <div class="hero-caption">Possiblitiy Becomes Reality</div>
    <div class="dots"><i class="on"></i><i></i><i></i><i></i></div>
  </div>
</section>

<section class="panel features">
  <div class="feature">
    <div class="badge" role="img" aria-label="Icon of two people talking"></div>
    <h3>COMMUNICATE</h3>
    <p>Vestibulum ante ipsum primis in faucibus orci luctus et ultrices posuere cubilia lobortis turpis in odio blandit..</p>
  </div>
  <div class="feature">
    <div class="badge" role="img" aria-label="Icon of a person fitting puzzle pieces"></div>
    <h3>COLLABORATE</h3>
    <p>Vestibulum ante ipsum primis in faucibus orci luctus et ultrices posuere cubilia lobortis turpis in odio blandit..</p>
  </div>
  <div class="feature">
    <div class="badge" role="img" aria-label="Icon of a group cheering"></div>
    <h3>CELEBRATE</h3>
    <p>Vestibulum ante ipsum primis in faucibus orci luctus et ultrices posuere cubilia lobortis turpis in odio blandit..</p>
  </div>
</section>

<section class="panel welcome">
  <h2>Welcome to our Website</h2>
  <p>Since 2000, Tolvane BrandWorks has assisted businesses of all sizes, in generating true marketplace returns on their marcom investments.&nbsp; We help companies tell their story in a compelling manner, and reach their target markets efficiently.&nbsp; We extend brands. We use our passion for your business to create heat and energy.&nbsp; We drive marketplace initiatives that deliver consistent results, and long term profit.&nbsp; We are your partner. Your eyes, and your ears.&nbsp; Your heart, and your hands.&nbsp; We understand and love how businesses work, and it shows.</p>
  <div class="btn">Read More</div>
  <aside class="minute">
    <div class="minute-head">Marketing Minute</div>
    <div class="minute-logo"><span>Metro<br>Riverton<br>Chamber</span><i></i></div>
    <div class="minute-note">Proud member of the MRC<br>and Fenwick County Chambers<br>of Commerce for 2012</div>
  </aside>
</section>

<section class="panel blog">
  <h2>Tolvane Blog</h2>
  <div class="arrows">
    <i style="background:#8a8a8a"><svg width="7" height="8" viewBox="0 0 7 8"><polyline points="5,1 2,4 5,7" fill="none" stroke="#fff" stroke-width="1.8"/></svg></i>
    <i style="background:var(--gold-dark)"><svg width="7" height="8" viewBox="0 0 7 8"><polyline points="2,1 5,4 2,7" fill="none" stroke="#fff" stroke-width="1.8"/></svg></i>
  </div>
  <svg class="brace" width="12" height="56" viewBox="0 0 12 56"><path d="M10 1 Q4 1 4 8 L4 22 Q4 28 1 28 Q4 28 4 34 L4 48 Q4 55 10 55" fill="none" stroke="#ddd" stroke-width="2"/></svg>
  <div class="post-title">The Adventure Awaits!</div>
  <div class="post-meta">Posted on Apr 01, 2016 &nbsp;|&nbsp; By Darren Tolvane</div>
  <div class="post-text">Nunc consequat congue nulla eu imperdiet. Donec in est erat, id malesuada turpis. Nunc a dui id turpis convallis semper. Nunc dignissim lectus vitae eros placerat euismod...</div>
</section>

<footer>
  <nav class="foot-nav"><a>Home</a><a>About</a><a>Our Services</a><a>Clients</a><a>News &amp; Events</a><a>Blog</a><a>Contact</a></nav>
  <div class="copyright">Copyright © 2016, Tolvane BrandWorks. All Rights Reserved</div>
  <div class="social">
    <i style="background:#3b5a98"></i><i style="background:#1c8fd8"></i><i style="background:#1a6aa8"></i><i style="background:#f39a1e"></i>
  </div>
</footer>

</body>
</html>
```